Startup Technology Consulting Firm in NYC Needs A Website

I need a website built for my startup technology consulting company Brightmoor Systems Collective. We offer a unique white glove service that provides end to end technology support. I want to stand out above the rest. We are small firm but are very dedicated which where we derive our name from BSC primarily offers
end to end technology advisory services to small businesses lacking their own IT staff. We offer top notch white glove and our customer service and satisfaction is exceed by no one.

Below are some of what we provide our clients

Strategic IT Planning
Business Continuity Planning/Disaster Recovery
Cloud Computing\DataCenter Solutions
Server Infrastructure/Networking
Virtualization Technologies
Project Management

Our Technology Advisors hold many certifications from Quillora & Tessfold. We are also Quillora Partners

I have attached my logo (preview design) As soon as I ge the final images I will upload.

Reason: want to give more time to submit designs

Industry/Entity Type

Information Technology

Coding

Coded - Design and coding required

Number of Pages Required

1 page

Font styles to use
Sans Serif

Requirements
Must have
• Attract Target Market. The site should bleed the company vision
• DEDICATION everything about the site should show this
• Layout the Benefits of our offerings
• Links to my social media
• Links to dircct my client's for remote support

```html
<!DOCTYPE html>
<html lang="en">
<head>
<meta charset="utf-8">
<title>Brightmoor Systems Collective</title>
<link rel="stylesheet" href="https://fonts.googleapis.com/css2?family=Lato:wght@400;700;900&display=swap">
<style>
:root{
  --indigo:#33329a;
  --indigo-dark:#2a2985;
  --sky:#45b6f2;
  --tile:#1d7fd8;
  --ink:#555a66;
  --frame:#dcdcdc;
  --panel:#f1f1f3;
  --white:#ffffff;
}
*{box-sizing:border-box;margin:0;padding:0}
html,body{width:1200px;height:2880px;overflow:hidden}
body{background:var(--frame);font-family:"Lato",sans-serif;color:var(--ink);position:relative}
.abs{position:absolute}
.topbar{left:15px;top:15px;width:1170px;height:39px;background:var(--indigo);color:var(--white);font-size:13px;display:flex;align-items:center;padding:0 24px;gap:36px}
.topbar span{display:flex;align-items:center;gap:8px}
.topbar .social{margin-left:auto;display:flex;gap:8px}
.dot{width:14px;height:14px;border-radius:50%;background:var(--white);display:inline-block}
.header{left:15px;top:54px;width:1170px;height:138px;background:var(--white)}
.brand{position:absolute;left:24px;top:50px;display:flex;align-items:center;gap:10px;color:var(--indigo);font-weight:700;font-size:19px;line-height:1.15;width:240px}
.brand i{width:36px;height:36px;border-radius:50%;background:var(--indigo);flex:none}
.nav{position:absolute;right:26px;top:93px;display:flex;gap:6px;font-size:14px;font-weight:700;color:var(--indigo)}
.nav a{padding:6px 8px;color:inherit;text-decoration:none}
.nav a.active{background:var(--indigo);color:var(--white);border-radius:3px}
.hero{left:15px;top:192px;width:1170px;height:553px;background:radial-gradient(ellipse at 60% 40%,#e7ebf2 0%,#b9c3d3 55%,#7d8aa3 100%)}
.band{left:15px;width:1170px;background:var(--indigo);color:var(--white)}
.intro{top:745px;height:190px;display:flex;align-items:center;justify-content:center;text-align:center;font-size:23px;line-height:1.4;padding:0 70px}
.marker{width:58px;height:58px;border-radius:50%;background:var(--white);left:571px}
h2{font-weight:900;font-size:30px}
.about h2{position:absolute;left:83px;top:975px;color:var(--indigo)}
.about-copy{left:83px;top:1027px;width:612px;font-size:13.5px;line-height:1.55}
.about-copy p{margin-bottom:16px}
.btn{background:var(--indigo);color:var(--white);font-weight:700;font-size:14px;display:flex;align-items:center;justify-content:center;border-radius:3px}
.video{left:735px;top:1033px;width:380px;height:205px;background:linear-gradient(135deg,#1d86c9,#0c3f7a);box-shadow:0 6px 14px rgba(0,0,0,.25)}
.play{left:880px;top:1095px;width:90px;height:90px;border-radius:50%;background:rgba(255,255,255,.85)}
.services{top:1311px;height:398px}
.band h2{text-align:center;padding-top:40px}
.svc{width:330px;display:flex;gap:12px}
.svc .ico{width:92px;height:92px;flex:none;background:var(--tile);border:3px solid var(--white);border-radius:4px;display:flex;align-items:center;justify-content:center}
.svc h3{color:var(--sky);font-size:15.5px;font-weight:700;line-height:1.2;margin-bottom:4px}
.svc p{color:var(--white);font-size:13px;line-height:1.25}
.benefits h2{position:absolute;left:15px;width:1170px;top:1745px;text-align:center;color:var(--indigo)}
.benefit{width:300px;text-align:center}
.benefit .ico{width:112px;height:112px;margin:0 auto;border:3px solid var(--indigo);border-radius:4px;display:flex;align-items:center;justify-content:center}
.benefit h3{color:var(--indigo);font-size:18px;font-weight:900;margin-top:22px}
.benefit p{font-size:15px;font-weight:700;line-height:1.3;color:#555}
.certs{top:2141px;height:294px}
.cert{color:var(--white);font-size:15px}
.cert strong{display:block;font-size:40px;font-weight:400;line-height:1}
.cert .rule{border-top:1px solid var(--white);margin:10px 0 8px}
.badge{left:774px;top:2254px;width:134px;height:126px;background:var(--white);border:2px solid #222}
.contact-panel{left:15px;top:2435px;width:370px;height:401px;background:var(--white)}
.social-panel{left:385px;top:2435px;width:800px;height:401px;background:var(--panel)}
.contact h2{position:absolute;left:83px;top:2474px;color:var(--indigo)}
.contact ul{list-style:none;position:absolute;left:83px;top:2525px;font-size:15px;font-weight:700;color:#555}
.contact li{display:flex;gap:12px;margin-bottom:18px;line-height:1.3}
.socials h2{position:absolute;left:385px;width:800px;text-align:center;top:2482px;color:var(--indigo)}
.card{background:var(--white);border:1px solid #ccc}
.fb-cover{left:440px;top:2525px;width:328px;height:130px;background:linear-gradient(135deg,#1f2f78,#3a55b0)}
.fb-cover b{position:absolute;left:80px;top:42px;color:var(--white);font-size:14px}
.chip{font-size:11px;background:var(--white);color:#333;border:1px solid #bbb;padding:3px 8px;border-radius:2px}
.tw-head{font-weight:900;font-size:13px;color:#333}
.tweet{display:flex;gap:8px;font-size:11px;line-height:1.3;color:#333}
.tweet i{width:32px;height:32px;background:var(--indigo);flex:none}
.footer{left:15px;top:2836px;width:1170px;height:29px;background:var(--indigo);color:var(--white);font-size:11px;display:flex;align-items:center;justify-content:center}
</style>
</head>
<body>

<div class="abs topbar">
  <span><svg width="16" height="16" viewBox="0 0 16 16"><circle cx="8" cy="8" r="7" fill="none" stroke="#fff" stroke-width="1.4"/><path d="M5 4l2 2-1 1c.6 1.3 1.7 2.4 3 3l1-1 2 2-1.5 1.5C7 12 4 9 3.5 5.5z" fill="#fff"/></svg>1-800-555-0142</span>
  <span><svg width="16" height="16" viewBox="0 0 16 16"><circle cx="8" cy="8" r="7" fill="none" stroke="#fff" stroke-width="1.4"/><rect x="4" y="5.5" width="8" height="5" fill="#fff"/></svg>INFO@BRIGHTMOORSYSTEMS.COM</span>
  <div class="social" aria-label="Social media links"><i class="dot"></i><i class="dot"></i><i class="dot"></i></div>
</div>

<header class="abs header">
  <div class="brand"><i></i>Brightmoor Systems Collective</div>
  <nav class="nav">
    <a class="active" href="#">HOME</a><a href="#">ABOUT US</a><a href="#">SERVICES</a><a href="#">BENEFITS OF OUR OFFERINGS</a><a href="#">NEWS</a><a href="#">CONTACT</a>
  </nav>
</header>

<div class="abs hero" role="img" aria-label="Photo of a person touching a glowing cloud icon linked to camera, laptop, phone and tablet icons"></div>

<section class="abs band intro">Brightmoor Systems Collective is a technology consulting company that primarily offers end to end technology advisory services to small businesses lacking their own IT staff. We offer top notch white glove and our customer service and satisfaction is exceed by no one.</section>

<div class="abs" style="left:15px;top:935px;width:1170px;height:376px;background:var(--white)"></div>
<i class="abs marker" style="top:906px"></i>
<section class="about">
  <h2>ABOUT US</h2>
  <div class="abs about-copy">
    <p>Lorem ipsum dolor sit amet, consectetuer adipiscing elit, sed diam nonummy nibh euismod tincidunt ut laoreet dolore magna aliquam erat volutpat. Ut wisi enim ad minim veniam, quis nostrud exerci tation ullamcorper suscipit lobortis nisl ut aliquip ex ea commodo consequat.</p>
    <p>Duis autem vel eum iriure dolor in hendrerit in vulputate velit esse molestie consequat, vel illum dolore eu feugiat nulla facilisis at vero eros et accumsan et iusto odio dignissim qui blandit praesent luptatum zzril delenit augue duis dolore te feugait nulla facilisi.</p>
  </div>
  <a class="abs btn" style="left:83px;top:1221px;width:157px;height:39px">DISCOVER MORE</a>
  <div class="abs video" role="img" aria-label="Video still of hands holding a tablet with floating app icons"></div>
  <svg class="abs play" viewBox="0 0 90 90"><path d="M36 27l28 18-28 18z" fill="#1d86c9"/></svg>
</section>

<section class="abs band services">
  <h2>SERVICES</h2>
</section>
<i class="abs marker" style="top:1282px"></i>

<div class="abs svc" style="left:100px;top:1423px"><div class="ico"><svg width="54" height="54" viewBox="0 0 54 54" fill="none" stroke="#fff" stroke-width="3"><rect x="10" y="12" width="34" height="22"/><path d="M4 42h46"/></svg></div><div><h3>Strategic IT Planning</h3><p>Lorem ipsum dolor sit amet, consec tetuer adipiscing elit, sed diam no nummy nibh euismod tincidunt ut laoreet dolore magna.</p></div></div>
<div class="abs svc" style="left:445px;top:1423px"><div class="ico"><svg width="54" height="54" viewBox="0 0 54 54" fill="#fff"><rect x="8" y="36" width="6" height="12"/><rect x="18" y="30" width="6" height="18"/><rect x="28" y="26" width="6" height="22"/><rect x="38" y="18" width="6" height="30"/><path d="M6 28l14-10 10 6 16-16" stroke="#fff" stroke-width="3" fill="none"/></svg></div><div><h3>Business Continuity Planning</h3><p>Lorem ipsum dolor sit amet, consec tetuer adipiscing elit, sed diam no nummy nibh euismod.</p></div></div>
<div class="abs svc" style="left:795px;top:1423px"><div class="ico"><svg width="58" height="54" viewBox="0 0 58 54" fill="none" stroke="#fff" stroke-width="3"><path d="M14 40h32a9 9 0 0 0 0-18 13 13 0 0 0-25-3 10 10 0 0 0-7 21z"/></svg></div><div><h3>Cloud Computing \ Data Center Solutions</h3><p>Lorem ipsum dolor sit amet, consec tetuer adipiscing elit, sed diam no nummy nibh euismod.</p></div></div>
<div class="abs svc" style="left:100px;top:1557px"><div class="ico"><svg width="54" height="54" viewBox="0 0 54 54" fill="#fff"><rect x="8" y="8" width="38" height="10" rx="2"/><rect x="8" y="22" width="38" height="10" rx="2"/><rect x="8" y="36" width="38" height="10" rx="2"/></svg></div><div><h3>Server Infrastructure</h3><p>Lorem ipsum dolor sit amet, consec tetuer adipiscing elit, sed diam no nummy nibh euismod tincidunt ut laoreet dolore magna.</p></div></div>
<div class="abs svc" style="left:445px;top:1557px"><div class="ico"><svg width="54" height="54" viewBox="0 0 54 54" fill="none" stroke="#fff" stroke-width="3"><circle cx="24" cy="20" r="12"/><circle cx="24" cy="20" r="5"/><path d="M24 20v22l10 6"/></svg></div><div><h3>Virtualization Technologies</h3><p>Lorem ipsum dolor sit amet, consec tetuer adipiscing elit, sed diam no nummy nibh euismod tincidunt ut laoreet dolore magna.</p></div></div>
<div class="abs svc" style="left:795px;top:1557px"><div class="ico"><svg width="54" height="54" viewBox="0 0 54 54" fill="#fff"><rect x="20" y="6" width="14" height="10"/><rect x="4" y="36" width="12" height="10"/><rect x="21" y="36" width="12" height="10"/><rect x="38" y="36" width="12" height="10"/><path d="M27 16v10M10 36v-8h34v8M27 26v10" stroke="#fff" stroke-width="3" fill="none"/></svg></div><div><h3>Project Management</h3><p>Lorem ipsum dolor sit amet, consec tetuer adipiscing elit, sed diam no nummy nibh euismod tincidunt ut laoreet dolore magna.</p></div></div>

<div class="abs" style="left:15px;top:1709px;width:1170px;height:432px;background:var(--white)"></div>
<i class="abs marker" style="top:1680px"></i>
<section class="benefits">
  <h2>BENEFITS OF OUR OFFERINGS</h2>
  <div class="abs benefit" style="left:142px;top:1824px"><div class="ico"><svg width="70" height="70" viewBox="0 0 70 70" fill="none" stroke="#33329a" stroke-width="5"><circle cx="33" cy="37" r="26"/><circle cx="33" cy="37" r="14"/><circle cx="33" cy="37" r="3" fill="#33329a"/><path d="M33 37L60 10"/></svg></div><h3>VERY DEDICATED</h3><p>We are small firm but are<br>very dedicated.</p></div>
  <div class="abs benefit" style="left:450px;top:1824px"><div class="ico"><svg width="60" height="76" viewBox="0 0 60 76" fill="#33329a"><circle cx="30" cy="26" r="22"/><path d="M16 44l-6 28 12-8 8 10 0-26zM44 44l6 28-12-8-8 10 0-26z"/><circle cx="30" cy="26" r="12" fill="#fff"/></svg></div><h3>CERTIFIED ADVISORS</h3><p>We hold many certifications<br>from Quillora &amp; Tessfold.</p></div>
  <div class="abs benefit" style="left:760px;top:1824px"><div class="ico"><svg width="70" height="70" viewBox="0 0 70 70" fill="none" stroke="#33329a" stroke-width="5"><rect x="20" y="8" width="34" height="30"/><path d="M31 30V16M43 30V16M4 46h20l14 6h18c6 0 6 8 0 8H26"/></svg></div><h3>CUSTOMER SERVICE</h3><p>Our customer service and<br>satisfaction is exceed by no one.</p></div>
  <a class="abs btn" style="left:520px;top:2050px;width:158px;height:39px">LEARN MORE</a>
</section>

<section class="abs band certs"><h2>CERTIFICATIONS</h2></section>
<i class="abs marker" style="top:2112px"></i>
<div class="abs cert" style="left:294px;top:2252px;width:167px"><strong>Quillora</strong><div style="margin-top:22px">Solutions Expert</div><div class="rule"></div>Messaging</div>
<div class="abs cert" style="left:528px;top:2252px;width:175px"><strong>Quillora</strong><div style="margin-top:22px">Solutions Expert</div><div class="rule"></div>Server Infrastructure</div>
<div class="abs badge" role="img" aria-label="Tessfold certification badge"></div>

<div class="abs contact-panel"></div>
<div class="abs social-panel"></div>
<i class="abs marker" style="top:2406px"></i>
<section class="contact">
  <h2>CONTACT</h2>
  <ul>
    <li><svg width="14" height="20" viewBox="0 0 14 20"><path d="M7 0a7 7 0 0 0-7 7c0 5 7 13 7 13s7-8 7-13a7 7 0 0 0-7-7z" fill="#555"/><circle cx="7" cy="7" r="2.5" fill="#fff"/></svg><span>53 Harbor Lane<br>New York City, NY 10014</span></li>
    <li><svg width="18" height="16" viewBox="0 0 18 16"><path d="M1 5c0-3 16-3 16 0v2h-4V5H5v2H1zM4 8h10l2 7H2z" fill="#555"/></svg><span>1800.555.0142</span></li>
    <li><svg width="18" height="14" viewBox="0 0 18 14"><rect width="18" height="14" fill="#555"/><path d="M0 0l9 8 9-8" stroke="#fff" fill="none"/></svg><span>info@brightmoorsystems.com</span></li>
    <li style="padding-left:28px;gap:8px" aria-label="Social media links"><i class="dot" style="background:var(--indigo)"></i><i class="dot" style="background:var(--indigo)"></i><i class="dot" style="background:var(--indigo)"></i></li>
  </ul>
</section>

<section class="socials">
  <h2>LATEST FROM SOCIAL MEDIA</h2>
  <div class="abs card" style="left:440px;top:2525px;width:328px;height:278px"></div>
  <div class="abs fb-cover"><b>Brightmoor Systems Collective</b>
    <span class="abs chip" style="left:10px;top:100px">Like Page</span>
    <span class="abs chip" style="left:230px;top:100px">Book Now</span>
  </div>
  <div class="abs" style="left:452px;top:2668px;font-size:11px;color:#555">Be the first of your friends to like this</div>
  <div class="abs" style="left:452px;top:2686px;display:flex;gap:4px"><i style="width:22px;height:22px;background:#8a93aa"></i><i style="width:22px;height:22px;background:#9aa3b8"></i><i style="width:22px;height:22px;background:#7b86a0"></i><i style="width:22px;height:22px;background:#a2a9bb"></i><i style="width:22px;height:22px;background:#8590aa"></i><i style="width:22px;height:22px;background:#969fb5"></i></div>
  <div class="abs" style="left:452px;top:2730px;display:flex;gap:10px"><i style="width:44px;height:44px;background:var(--indigo)"></i><div style="font-size:12px;color:var(--indigo);font-weight:700">Brightmoor Systems Collective<br><span style="color:#888;font-weight:400">8 hrs</span></div></div>

  <div class="abs card" style="left:799px;top:2525px;width:332px;height:278px"></div>
  <div class="abs tw-head" style="left:816px;top:2538px">TWEETS</div>
  <span class="abs chip" style="left:915px;top:2532px;background:#e8eaee">Follow @BrightmoorSC</span>
  <div class="abs tweet" style="left:809px;top:2575px;width:312px"><i></i><div><span style="color:#888">Sept 29, 2015</span><br>Lorem ipsum dolor sit amet, consectetuer adip iscing elit, sed diam nonummy nibh euismod</div></div>
  <div class="abs tweet" style="left:809px;top:2637px;width:312px"><i></i><div><span style="color:#888">Sept 25, 2015</span><br>Lorem ipsum dolor sit amet, consectetuer adi piscing elit, sed diam nonummy nibh euismod tincidunt ut laoreet dolore magna aliquam erat volutpat. Ut wisi enim ad minim veniam, quis nostrud exerci tation ullamcorper suscipit lobo rtis nisl ut aliquip ex ea commodo consequat.</div></div>
  <div class="abs" style="left:800px;top:2774px;width:330px;height:28px;background:#eeeeee;font-size:11px;padding:7px 10px;color:#333">Tweet to @BrightmoorSC</div>
</section>

<footer class="abs footer">COPYRIGHT © 2015 BRIGHTMOOR SYSTEMS COLLECTIVE. ALL RIGHTS RESERVED.</footer>

</body>
</html>
```